Custom Cabinet Shop Needs a website design

Hi,
We need a website for a Custom Cabinet Shop and Cabinet parts manufacturing business.
The business has two sides to it. One side provides custom Kitchens, vanities, entertainment units, offices and what not to homeowners and contractors.
The 2nd side of the business provides built to order cabinet boxes and other parts required to put together a project to other cabinet shops, small contractors looking to install there own cabinets.
Website will need a Gallery to display work.
Color scheme to go well with logo.
current website is www.brindlewoodcustomcabinets.com
being changed to www.brindlewood.ca
Logo Included in attached files.
Tagline "Millwork with Flare"
Mission Statement "Our passion is to deliver inspired cabinetry solutions to suit all your needs, supported by our phenomenal star class customer service"
The website should convey quality and professionalism.
Thank you.
Homeowners/ Contractors
Entertainment
Coded - Design and coding required
1 page

```html
<!DOCTYPE html>
<html lang="en">
<head>
<meta charset="utf-8">
<title>Brindlewood Custom Cabinets</title>
<link rel="stylesheet" href="https://fonts.googleapis.com/css2?family=Lato:wght@400;700&family=Montserrat:wght@500;600&display=swap">
<style>
:root{
  --orange:#f05a22;
  --ink:#1b1b1b;
  --text:#444;
  --light:#f4f4f4;
  --rule:#d6d6d6;
  --footer:#232323;
  --black:#000;
  --white:#fff;
}
*{margin:0;padding:0;box-sizing:border-box}
html,body{width:859px;height:1200px;overflow:hidden}
body{position:relative;font-family:'Lato',sans-serif;color:var(--text);background:var(--light)}
.abs{position:absolute}
h2{font-family:'Montserrat',sans-serif;font-weight:600;font-size:16px;color:var(--ink);letter-spacing:.2px}
h2 span{color:var(--orange)}
.heading-rule{border-bottom:1px solid var(--rule);padding-bottom:6px;position:relative}
.heading-rule::after{content:"";position:absolute;left:0;bottom:-2px;width:48px;height:2px;background:#bbb}
p{font-size:9.2px;line-height:13.3px}

/* header */
.site-header{left:0;top:0;width:859px;height:87px;background:linear-gradient(#fff,#ececec);border-top:2px solid #111}
.brand{left:94px;top:28px;display:flex;align-items:center;gap:7px;font-family:'Montserrat',sans-serif;font-weight:600;font-size:17px;color:var(--ink)}
.brand i{width:14px;height:14px;background:var(--orange);border-radius:50%}
.topbar{left:464px;top:10px;display:flex;gap:12px;font-size:10.5px;color:#222;align-items:center}
.topbar .item{display:flex;align-items:center;gap:5px}
.topbar .sep{width:1px;height:13px;background:#ccc}
.nav-line{left:299px;top:69px;width:80px;height:2px;background:#222}
.main-nav{left:372px;top:37px;width:393px;height:34px;background:linear-gradient(#2a2a2a,#0d0d0d);clip-path:polygon(6px 0,100% 0,100% 100%,0 100%);display:flex;align-items:center;border-radius:0 4px 4px 0}
.main-nav a{color:#fff;text-decoration:none;font-family:'Montserrat',sans-serif;font-weight:500;font-size:9.5px;height:100%;display:flex;align-items:center;justify-content:center;border-right:1px solid #333}
.main-nav a.current{color:var(--orange)}

/* hero */
.hero{left:0;top:87px;width:859px;height:272px;background:linear-gradient(180deg,#4c5a2e 0%,#6a5a32 35%,#8a4a1a 60%,#5a2a0c 100%)}
.hero-arrow{top:211px;width:24px;height:24px;background:rgba(60,60,60,.85);display:flex;align-items:center;justify-content:center}
.tagline{left:566px;top:293px;height:25px;padding:0 12px;background:#111;color:#fff;font-family:'Montserrat',sans-serif;font-weight:600;font-size:11px;display:flex;align-items:center;border:2px solid #fff;transform:skewX(-8deg)}
.dots{left:400px;top:341px;display:flex;gap:5px}
.dots span{width:10px;height:10px;background:#aaa}
.dots span.on{background:var(--orange);border:1px solid #fff}

/* intro */
.intro{left:0;top:359px;width:859px;height:209px;background:var(--light)}
.divider-v{left:501px;top:384px;width:1px;height:160px;background:#e2e2e2}
.btn{background:var(--orange);color:#fff;font-weight:700;font-size:9px;display:flex;align-items:center;justify-content:center;border-radius:2px}
.video{left:532px;top:418px;width:232px;height:129px;background:linear-gradient(#2d3236,#6b7378 60%,#3a3f44);border:4px solid #111;box-shadow:0 4px 6px rgba(0,0,0,.2)}
.video .bar{position:absolute;left:0;right:0;bottom:0;height:14px;background:#111}
.video .bar i{position:absolute;left:14px;top:6px;width:110px;height:2px;background:#555}
.video .bar i::before{content:"";position:absolute;left:0;top:0;width:45px;height:2px;background:#d22}
.video .play{position:absolute;left:101px;top:46px;width:30px;height:22px;background:#d22;border-radius:5px;display:flex;align-items:center;justify-content:center}

/* split */
.split-dark{left:0;top:568px;width:430px;height:268px;background:var(--black)}
.split-orange{left:430px;top:568px;width:429px;height:268px;background:var(--orange)}
.split-dark h2,.split-orange h2{color:#fff}
.split-dark .heading-rule{border-color:#444}
.split-orange .heading-rule{border-color:#f6a27f}
.split-orange .heading-rule::after,.split-dark .heading-rule::after{background:#fff}
.photo{height:131px;border:3px solid #333}
.split-orange .photo{border-color:#f9b79d}
.split-dark p{color:#ddd}
.split-orange p{color:#fff}

/* gallery */
.gallery{left:94px;top:870px;width:671px;height:114px;background:#e6e6e6;border:1px solid #ddd;border-radius:3px}
.gallery-tab{left:338px;top:863px;width:185px;height:23px;background:var(--orange);border-radius:0 0 24px 24px;color:#fff;font-family:'Montserrat',sans-serif;font-weight:500;font-size:10.5px;display:flex;align-items:center;justify-content:center;letter-spacing:.5px}
.thumb{top:900px;width:122px;height:72px}
.g-arrow{top:931px;width:14px;height:14px;border-radius:50%;background:#fff;border:1px solid #ccc;display:flex;align-items:center;justify-content:center}

/* footer */
.site-footer{left:0;top:1015px;width:859px;height:157px;background:var(--footer);color:#fff}
.map{left:94px;top:1038px;width:196px;height:111px;background:linear-gradient(135deg,#a9c6e8,#efe7d6 35%,#f2d9a7 60%,#e6eedd);border:2px solid #555}
.contact-row{left:312px;display:flex;gap:12px;font-size:9.4px;line-height:11.5px}
.contact-row svg{flex:none;width:14px}
.stay{left:483px;top:1037px;font-size:12px}
.email-input{left:483px;top:1063px;width:135px;height:20px;background:#fff;color:#999;font-size:7.5px;font-style:italic;padding:6px}
.submit{left:483px;top:1090px;width:60px;height:20px;background:var(--orange);font-family:'Montserrat',sans-serif;font-size:11px;display:flex;align-items:center;justify-content:center}
.note{left:482px;top:1125px;font-size:7.6px;line-height:9.5px;color:#ddd}
.footer-brand{left:645px;top:1064px;display:flex;align-items:center;gap:6px;font-family:'Montserrat',sans-serif;font-weight:600;font-size:15px}
.footer-brand i{width:12px;height:12px;border-radius:50%;background:#fff}
.social{left:656px;top:1124px;display:flex;gap:7px}
.social span{width:21px;height:21px;border-radius:50%;background:#fff}
.copyright{left:0;top:1172px;width:859px;height:28px;background:#000;color:#ddd;font-size:9px;display:flex;align-items:center;justify-content:center;letter-spacing:.3px}
</style>
</head>
<body>

<header class="abs site-header">
  <div class="abs brand"><i></i>BRINDLEWOOD</div>
  <div class="abs topbar">
    <span class="item"><svg width="11" height="11" viewBox="0 0 24 24"><path fill="#f05a22" d="M6.6 10.8a15 15 0 0 0 6.6 6.6l2.2-2.2c.3-.3.7-.4 1-.2 1.1.4 2.3.6 3.6.6.6 0 1 .4 1 1V20c0 .6-.4 1-1 1C10.6 21 3 13.4 3 4c0-.6.4-1 1-1h3.5c.6 0 1 .4 1 1 0 1.3.2 2.5.6 3.6.1.3 0 .7-.2 1z"/></svg>403-555-0147</span>
    <span class="sep"></span>
    <span class="item"><svg width="11" height="9" viewBox="0 0 24 18"><path fill="#f05a22" d="M0 0h24v18H0z"/><path fill="none" stroke="#fff" stroke-width="2" d="M1 1l11 9 11-9"/></svg>sales@brindlewoodcustomcabinets.com</span>
  </div>
  <div class="abs nav-line"></div>
  <nav class="abs main-nav">
    <a class="current" style="width:69px">HOME</a>
    <a style="width:81px">GALLERY</a>
    <a style="width:78px">SERVICES</a>
    <a style="width:93px">WARRANTY</a>
    <a style="width:72px;border:0">CONTACT</a>
  </nav>
</header>

<section class="abs hero" role="img" aria-label="Wooden kitchen cabinets with granite counter and windows to a garden"></section>
<div class="abs hero-arrow" style="left:10px"><svg width="8" height="10" viewBox="0 0 8 10"><path d="M6 1L2 5l4 4" stroke="#fff" stroke-width="2" fill="none"/></svg></div>
<div class="abs hero-arrow" style="left:825px"><svg width="8" height="10" viewBox="0 0 8 10"><path d="M2 1l4 4-4 4" stroke="#fff" stroke-width="2" fill="none"/></svg></div>
<div class="abs tagline">MILLWORK WITH FLARE</div>
<div class="abs dots"><span></span><span class="on"></span><span></span><span></span></div>

<section class="abs intro"></section>
<div class="abs" style="left:94px;top:377px;width:380px">
  <h2 class="heading-rule">BRINDLEWOOD <span>CUSTOM CABINETS</span></h2>
  <p style="margin-top:12px">Lorem ipsum dolor sit amet, consectetur adipiscing elit. Sed ut lorem eu ex pellentesque rhoncus. Mauris ultricies gravida risus, sed imperdiet nulla mollis ut. Fusce iaculis tristique tellus, vitae tempus risus gravida sed. Vestibulum consequat sapien velit, nec dictum ante sollicitudin volutpat. Nam sollicitudin, nisi sit amet semper gravida, ligula diam luctus elit, sit amet pellentesque orci turpis id erat. Nulla malesuada, metus eget.</p>
  <p style="margin-top:5px">Pellentesque habitant morbi tristique senectus et netus et malesuada fames ac turpis egestas. Duis magna dolor, congue quis malesuada non, suscipit eu velit.</p>
</div>
<div class="abs btn" style="left:94px;top:523px;width:72px;height:23px">Read More</div>
<div class="abs divider-v"></div>
<div class="abs" style="left:531px;top:377px;width:234px">
  <h2 class="heading-rule">WORKING <span>PROCESS</span></h2>
</div>
<div class="abs video" role="img" aria-label="Video of built-in white shelving cabinets">
  <div class="play"><svg width="10" height="10" viewBox="0 0 10 10"><path d="M2 1l7 4-7 4z" fill="#fff"/></svg></div>
  <div class="bar"><i></i></div>
</div>

<section class="abs split-dark">
  <div style="position:absolute;left:94px;top:17px;width:318px">
    <h2 class="heading-rule">CUSTOM CABINET</h2>
    <div class="photo" style="margin-top:13px;background:linear-gradient(#cfc9bf,#e9e6e0 50%,#7d6e5c)" role="img" aria-label="White kitchen with island under construction and steel fridge"></div>
    <p style="margin-top:12px">Lorem ipsum dolor sit amet, consectetur adipiscing elit. Vivamus molestie erat quis quam semper, quis hendrerit nisl tristique. Donec vitae orci eu nisi vehicula tincidunt at ac ligula. Class aptent taciti sociosqu ad litora torquent per conubia nostra, per inceptos himenaeos.</p>
  </div>
</section>
<section class="abs split-orange">
  <div style="position:absolute;left:18px;top:17px;width:318px">
    <h2 class="heading-rule">ORDER ONLINE</h2>
    <div class="photo" style="margin-top:13px;background:linear-gradient(90deg,#8f8a80,#2a2522 30%,#e8e4dc 65%,#b9b2a4)" role="img" aria-label="Dark bathroom vanity beside a white tub with red towel"></div>
    <p style="margin-top:12px">Lorem ipsum dolor sit amet, consectetur adipiscing elit. Vivamus molestie erat quis quam semper, quis hendrerit nisl tristique. Donec vitae orci eu nisi vehicula tincidunt at ac ligula. Class aptent taciti sociosqu ad litora torquent per conubia nostra, per inceptos himenaeos.</p>
  </div>
</section>

<section class="abs gallery"></section>
<div class="abs gallery-tab">PHOTO GALLERY</div>
<div class="abs thumb" style="left:104px;background:linear-gradient(#cdbfb0,#5a2a1a)" role="img" aria-label="Entertainment unit with television"></div>
<div class="abs thumb" style="left:236px;background:linear-gradient(#3a2e26,#b07f5a)" role="img" aria-label="Wet bar with wine rack"></div>
<div class="abs thumb" style="left:368px;background:linear-gradient(#dfe6ea,#8b6b4a)" role="img" aria-label="Dining room with built-in cabinets"></div>
<div class="abs thumb" style="left:501px;background:linear-gradient(90deg,#2c3336,#5a6e7a,#2c3336)" role="img" aria-label="Dark display cabinet with glass doors"></div>
<div class="abs thumb" style="left:633px;background:linear-gradient(#bdb3a6,#3a2e28)" role="img" aria-label="Bedroom with dark wardrobe cabinets"></div>
<div class="abs g-arrow" style="left:87px"><svg width="5" height="6" viewBox="0 0 5 6"><path d="M4 0v6L0 3z" fill="#888"/></svg></div>
<div class="abs g-arrow" style="left:758px"><svg width="5" height="6" viewBox="0 0 5 6"><path d="M1 0v6l4-3z" fill="#888"/></svg></div>

<footer class="abs site-footer"></footer>
<div class="abs map" role="img" aria-label="Street map showing the shop location"></div>
<div class="abs contact-row" style="top:1036px;color:#fff">
  <svg height="15" viewBox="0 0 14 20"><path d="M7 0a7 7 0 0 0-7 7c0 5 7 13 7 13s7-8 7-13a7 7 0 0 0-7-7zm0 10a3 3 0 1 1 0-6 3 3 0 0 1 0 6z" fill="#fff"/></svg>
  <div><b>CUSTOM CABINETS</b><br>48120 Range Road 190<br>Foothills, Alberta<br>T1X 0A0</div>
</div>
<div class="abs contact-row" style="top:1093px"><svg height="12" viewBox="0 0 24 24"><path fill="#fff" d="M6.6 10.8a15 15 0 0 0 6.6 6.6l2.2-2.2c.3-.3.7-.4 1-.2 1.1.4 2.3.6 3.6.6.6 0 1 .4 1 1V20c0 .6-.4 1-1 1C10.6 21 3 13.4 3 4c0-.6.4-1 1-1h3.5c.6 0 1 .4 1 1 0 1.3.2 2.5.6 3.6.1.3 0 .7-.2 1z"/></svg><b>403-555-0147</b></div>
<div class="abs contact-row" style="top:1115px"><svg height="12" viewBox="0 0 24 24"><path fill="#fff" d="M6 2h12v5H6zM2 8h20v10h-4v4H6v-4H2zm6 8v4h8v-4z"/></svg><b>403-555-0182</b></div>
<div class="abs contact-row" style="top:1136px"><svg height="10" viewBox="0 0 24 18"><path fill="none" stroke="#fff" stroke-width="2" d="M1 1h22v16H1zM1 1l11 9 11-9"/></svg><span>info@brindlewood.ca</span></div>

<div class="abs stay" style="color:#fff">Stay in Touch</div>
<div class="abs email-input">Enter your email.....</div>
<div class="abs submit" style="color:#fff">SUBMIT</div>
<div class="abs note">We never Share your email address<br>with another third party.</div>
<div class="abs footer-brand" style="color:#fff"><i></i>BRINDLEWOOD</div>
<div class="abs social"><span></span><span></span><span></span><span></span></div>
<div class="abs copyright">© 2015 Custom Cabinets. All Rights Reserved</div>

</body>
</html>
```